Looking for a clean, modern, and professional business card design that reflects Valtrim Systems

The design should include the company logo, contact details, and align with our brand identity. Please use a sophisticated and minimalist style, incorporating [specific colors, if applicable]. Creativity is welcome, but the card must maintain a polished and professional appearance.

Details to Include:

Name: Gavin Trelowe
Title: VP Sales / Operations
Company: Valtrim Systems
Phone: 483.216.7705
Email: gavin@valtrimsystems-example.com
Website: www.valtrimsystems-example.com

```html
<!DOCTYPE html>
<html lang="en">
<head>
<meta charset="utf-8">
<title>Valtrim Systems — Business Card</title>
<link rel="stylesheet" href="https://fonts.googleapis.com/css2?family=Poppins:wght@400;600&display=swap">
<style>
  :root {
    --page-bg: #e9eaec;
    --card-white: #fbfcfd;
    --brand-blue: #2a6fb3;
    --ink-black: #111214;
    --card-shadow: rgba(0, 0, 0, 0.18);
  }
  * { box-sizing: border-box; margin: 0; padding: 0; }
  html, body {
    width: 1200px; height: 900px; overflow: hidden;
    background: var(--page-bg);
    font-family: "Poppins", sans-serif;
  }
  .canvas {
    position: relative; width: 1200px; height: 900px;
  }
  .card {
    position: absolute; left: 320px; width: 560px; height: 320px;
    background: var(--card-white);
    box-shadow: 0 10px 28px var(--card-shadow);
    overflow: hidden;
  }
  .card--front { top: 100px; }
  .card--back { top: 480px; }

  /* front */
  .accent-block {
    position: absolute; left: 0; top: 78px; width: 78px; height: 62px;
    background: var(--ink-black);
  }
  .name-band {
    position: absolute; left: 120px; right: 0; top: 118px; height: 92px;
    background: var(--brand-blue);
    border-radius: 46px 0 0 46px;
  }
  .emblem-disc {
    position: absolute; left: 70px; top: 58px; width: 124px; height: 124px;
    border-radius: 50%;
    background: var(--card-white);
    border: 6px solid var(--brand-blue);
  }
  .wordmark {
    position: absolute; right: 34px; top: 40px;
    font-weight: 600; font-size: 24px; letter-spacing: 0.5px;
    color: var(--ink-black);
  }
  .person {
    position: absolute; right: 34px; top: 132px; text-align: right;
    color: var(--card-white);
  }
  .person__name { font-weight: 600; font-size: 28px; line-height: 1.15; letter-spacing: 0.3px; }
  .person__title { font-weight: 400; font-size: 15px; letter-spacing: 0.6px; }
  .contacts {
    position: absolute; right: 30px; top: 228px;
    list-style: none; text-align: right;
  }
  .contacts__item {
    display: flex; align-items: center; justify-content: flex-end; gap: 10px;
    font-size: 13px; line-height: 22px; color: var(--brand-blue);
  }
  .contacts__icon { width: 15px; height: 15px; flex: none; }

  /* back */
  .back-mark {
    position: absolute; inset: 0;
    display: flex; align-items: center; justify-content: center; gap: 12px;
  }
  .back-mark__dot {
    width: 16px; height: 16px; border-radius: 50%; background: var(--brand-blue);
  }
  .back-mark__name {
    font-weight: 600; font-size: 36px; letter-spacing: 0.6px; color: var(--ink-black);
  }
</style>
</head>
<body>
<main class="canvas">
  <section class="card card--front" aria-label="Card front">
    <div class="accent-block"></div>
    <div class="name-band"></div>
    <div class="emblem-disc"></div>
    <div class="wordmark">Valtrim Systems</div>
    <div class="person">
      <p class="person__name">Gavin Trelowe</p>
      <p class="person__title">VP Sales / Operations</p>
    </div>
    <ul class="contacts">
      <li class="contacts__item">483.216.7705
        <svg class="contacts__icon" viewBox="0 0 16 16" aria-hidden="true">
          <circle cx="8" cy="8" r="8" fill="#111214"/>
          <path d="M5.2 4.2l1.3-.2.8 2-1 .8a5 5 0 0 0 2.9 2.9l.8-1 2 .8-.2 1.3c-.1.5-.6.8-1.1.7A7 7 0 0 1 4.5 5.3c-.1-.5.2-1 .7-1.1z" fill="#fbfcfd"/>
        </svg>
      </li>
      <li class="contacts__item">gavin@valtrimsystems-example.com
        <svg class="contacts__icon" viewBox="0 0 16 16" aria-hidden="true">
          <circle cx="8" cy="8" r="8" fill="#111214"/>
          <rect x="4" y="5.2" width="8" height="5.6" rx="0.6" fill="none" stroke="#fbfcfd" stroke-width="1"/>
          <path d="M4.3 5.6L8 8.4l3.7-2.8" fill="none" stroke="#fbfcfd" stroke-width="1"/>
        </svg>
      </li>
      <li class="contacts__item">www.valtrimsystems-example.com
        <svg class="contacts__icon" viewBox="0 0 16 16" aria-hidden="true">
          <circle cx="8" cy="8" r="8" fill="#111214"/>
          <circle cx="8" cy="8" r="4" fill="none" stroke="#fbfcfd" stroke-width="1"/>
          <ellipse cx="8" cy="8" rx="1.8" ry="4" fill="none" stroke="#fbfcfd" stroke-width="0.9"/>
          <path d="M4 8h8" stroke="#fbfcfd" stroke-width="0.9"/>
        </svg>
      </li>
    </ul>
  </section>

  <section class="card card--back" aria-label="Card back">
    <div class="back-mark">
      <span class="back-mark__dot"></span>
      <span class="back-mark__name">Valtrim Systems</span>
    </div>
  </section>
</main>
</body>
</html>
```